Uk Sports Coaching company needs a poster design for a new 'Speed Development Centre'

We need a poster design for my UK based company called 'Brisk Field Academy'. We are a sports coaching company who specialise in rugby coaching and athlete development. We need a poster design that is quite modern, which explains all about our new venture which is our 'Speed Development Centre'.

The poster needs to explain what will be coached at the centre: Balance, Speed of limb movement, trunk strength, explosive strength, running speed, agility and anaerobic capacity. (these can be bullet pointed).

The poster should include:

When: Starting Friday 3rd October @6pm-7pm (Then every following Friday

venue: Harwick Grange Athletics Track

Price: £100 for the full course + free training T-Shirt

I would also like it to say how to book and get in contact through my phone number and email address which are:

contact@briskfieldacademy.co.uk

07700914386

www.briskfieldacademy.com

Our company colours are black, red and white, and that is also the colour of our logo.

Speed Development centre is open to all players aged 8-16.

I have attached multiple copies of my logo in different formats, i have also attached a word document briefly explaining what the speed development centre will achieve.

Thank you!

Target Market(s)

Parents and Aspiring Rugby players

Industry/Entity Type

Training

Requirements
Must have
• Price
Venue
When it will commence

```html
<!DOCTYPE html>
<html lang="en">
<head>
<meta charset="utf-8">
<title>Speed Development Centre – Brisk Field Academy</title>
<link rel="stylesheet" href="https://fonts.googleapis.com/css2?family=Questrial&family=Anton&family=Arimo:wght@400;700&display=swap">
<style>
  :root{
    --ink:#141414;
    --ink-soft:#232323;
    --red:#d8262c;
    --red-light:#ee4a4f;
    --red-dark:#9d1418;
    --white:#ffffff;
    --paper:#eeeeee;
    --grey:#c9c9c9;
    --text-dark:#2b2b2b;
    --grass:#5f8a3a;
    --grass-dark:#2f4a22;
    --sky:#d9dde0;
  }
  *{margin:0;padding:0;box-sizing:border-box}
  html,body{width:981px;height:1200px;overflow:hidden;background:var(--ink)}
  .poster{position:relative;width:981px;height:1200px;overflow:hidden;
    background:linear-gradient(180deg,var(--ink-soft),var(--ink));
    font-family:"Questrial",sans-serif;color:var(--white)}
  .shapes{position:absolute;inset:0}
  .title-band{position:absolute;left:0;top:43px;width:981px;height:82px;
    background:linear-gradient(180deg,var(--white),var(--grey));
    display:flex;align-items:center;justify-content:center}
  .title{font-family:"Questrial",sans-serif;font-weight:400;font-size:64px;
    color:var(--red);letter-spacing:1px;white-space:nowrap}
  .brand{position:absolute;left:660px;top:282px;display:flex;align-items:center;gap:12px}
  .brand-name{font-family:"Questrial",sans-serif;font-size:27px;color:var(--text-dark)}
  .brand-dot{width:18px;height:18px;border-radius:50%;background:var(--red)}
  .intro{position:absolute;left:597px;top:428px;width:370px;
    font-family:"Arimo",sans-serif;font-weight:700;font-size:19px;line-height:1.2}
  .skills{position:absolute;left:597px;top:522px;list-style:none;font-size:24px;line-height:31px}
  .skills li{display:flex;align-items:center;gap:8px}
  .skills svg{width:18px;height:18px;flex:none}
  .price{position:absolute;left:287px;top:574px;width:210px;height:210px;border-radius:50%;
    background:radial-gradient(circle at 40% 35%,var(--white),var(--grey));
    border:4px solid var(--ink);
    display:flex;flex-direction:column;align-items:center;justify-content:center;
    color:var(--red);font-family:"Arimo",sans-serif;font-weight:700;text-align:center}
  .price-amount{font-size:60px;line-height:1}
  .price-note{font-size:15px;line-height:1.2}
  .price-small{font-size:12px;font-weight:400;color:var(--text-dark);margin-top:6px}
  .when,.where{position:absolute;left:22px;display:flex;align-items:center;gap:10px;color:var(--ink)}
  .when{top:828px}
  .where{top:938px}
  .label{font-family:"Anton",sans-serif;font-size:52px;line-height:1;
    text-shadow:0 0 6px rgba(255,255,255,.7)}
  .when-detail{font-family:"Arimo",sans-serif;font-weight:700;line-height:1}
  .when-row{display:flex;align-items:flex-end;gap:4px}
  .day-num{font-size:44px}
  .stack{display:flex;flex-direction:column;font-size:26px}
  .stack small{font-size:16px}
  .when-after{font-size:19px;margin-top:4px}
  .venue{font-family:"Arimo",sans-serif;font-weight:700;font-size:24px;line-height:1.1;color:var(--white)}
  .contact-head{position:absolute;left:41px;top:1024px;font-family:"Arimo",sans-serif;font-size:26px;color:var(--white)}
  .contact-head b{color:var(--red-light)}
  .contact-list{position:absolute;left:41px;top:1068px;list-style:none;font-family:"Arimo",sans-serif;font-size:20px;line-height:36px}
  .contact-list li{display:flex;align-items:center;gap:14px}
  .contact-list svg{width:18px;height:18px;flex:none}
</style>
</head>
<body>
<div class="poster">
  <svg class="shapes" width="981" height="1200" viewBox="0 0 981 1200">
    <defs>
      <linearGradient id="redPanel" x1="0" y1="0" x2="0" y2="1">
        <stop offset="0" stop-color="#ee4a4f"/><stop offset="1" stop-color="#b81b21"/>
      </linearGradient>
      <linearGradient id="whiteBand" x1="0" y1="0" x2="0" y2="1">
        <stop offset="0" stop-color="#ffffff"/><stop offset="1" stop-color="#bfbfbf"/>
      </linearGradient>
      <linearGradient id="redBanner" x1="0" y1="0" x2="0" y2="1">
        <stop offset="0" stop-color="#ee4a4f"/><stop offset="1" stop-color="#9d1418"/>
      </linearGradient>
      <linearGradient id="fieldTones" x1="0" y1="0" x2="0" y2="1">
        <stop offset="0" stop-color="#2f4a22"/><stop offset=".35" stop-color="#5f8a3a"/><stop offset="1" stop-color="#7ea04f"/>
      </linearGradient>
      <linearGradient id="lineoutTones" x1="0" y1="0" x2="0" y2="1">
        <stop offset="0" stop-color="#e4e6e8"/><stop offset=".6" stop-color="#b9bcb6"/><stop offset="1" stop-color="#556b40"/>
      </linearGradient>
    </defs>
    <g role="img" aria-label="Photo: young rugby players tackling on a grass pitch">
      <polygon points="0,143 680,143 480,800 0,800" fill="url(#fieldTones)"/>
    </g>
    <polygon points="700,160 981,160 981,800 500,800" fill="url(#redPanel)"/>
    <polygon points="676,236 981,236 981,372 634,372" fill="url(#whiteBand)"/>
    <polygon points="0,815 700,815 676,928 0,928" fill="url(#redBanner)"/>
    <polygon points="0,932 674,932 656,1000 0,1000" fill="url(#redBanner)"/>
    <g role="img" aria-label="Photo: junior rugby lineout with a player lifted to catch the ball">
      <polygon points="720,815 981,815 981,1200 580,1200" fill="url(#lineoutTones)"/>
    </g>
  </svg>

  <header class="title-band"><h1 class="title">SPEED DEVELOPMENT CENTRE</h1></header>

  <div class="brand"><span class="brand-name">Brisk Field Academy</span><span class="brand-dot"></span></div>

  <p class="intro">Speed Development centre is open to all players aged 8-16.</p>

  <ul class="skills">
    <li><svg viewBox="0 0 18 18"><path d="M2 10l5 5L16 3" fill="none" stroke="#fff" stroke-width="2.4"/></svg>Balance</li>
    <li><svg viewBox="0 0 18 18"><path d="M2 10l5 5L16 3" fill="none" stroke="#fff" stroke-width="2.4"/></svg>Speed of limb movement</li>
    <li><svg viewBox="0 0 18 18"><path d="M2 10l5 5L16 3" fill="none" stroke="#fff" stroke-width="2.4"/></svg>Trunk strength</li>
    <li><svg viewBox="0 0 18 18"><path d="M2 10l5 5L16 3" fill="none" stroke="#fff" stroke-width="2.4"/></svg>Explosive strength</li>
    <li><svg viewBox="0 0 18 18"><path d="M2 10l5 5L16 3" fill="none" stroke="#fff" stroke-width="2.4"/></svg>Running speed</li>
    <li><svg viewBox="0 0 18 18"><path d="M2 10l5 5L16 3" fill="none" stroke="#fff" stroke-width="2.4"/></svg>Agility</li>
    <li><svg viewBox="0 0 18 18"><path d="M2 10l5 5L16 3" fill="none" stroke="#fff" stroke-width="2.4"/></svg>Anaerobic capacity.</li>
  </ul>

  <div class="price">
    <span class="price-amount">£100</span>
    <span class="price-note">for the full course*<br>+ free training T-Shirt</span>
    <span class="price-small">*6 weeks</span>
  </div>

  <section class="when">
    <span class="label">WHEN?</span>
    <div class="when-detail">
      <div class="when-row">
        <div class="stack"><small>Starting</small><span class="day-num">3rd</span></div>
        <div class="stack"><span>Friday</span><span>October <small>@6pm-7pm</small></span></div>
      </div>
      <div class="when-after">(Then every following Friday)</div>
    </div>
  </section>

  <section class="where">
    <span class="label">WHERE?</span>
    <span class="venue">Harwick Grange<br>Athletics Track</span>
  </section>

  <p class="contact-head"><b>book</b> and get in <b>contact</b></p>
  <ul class="contact-list">
    <li><svg viewBox="0 0 18 18"><rect x="1.5" y="4" width="15" height="10" fill="none" stroke="#d8262c" stroke-width="1.6"/><path d="M1.5 4l7.5 6 7.5-6" fill="none" stroke="#d8262c" stroke-width="1.6"/></svg>contact@briskfieldacademy.co.uk</li>
    <li><svg viewBox="0 0 18 18"><path d="M4 2l3 3-2 2c1 2 3 4 5 5l2-2 3 3-2 3C8 15 3 10 2 4z" fill="#d8262c"/></svg>07700914386</li>
    <li><svg viewBox="0 0 18 18"><circle cx="9" cy="9" r="7" fill="none" stroke="#d8262c" stroke-width="1.5"/><path d="M2 9h14M9 2c-3 4-3 10 0 14M9 2c3 4 3 10 0 14" fill="none" stroke="#d8262c" stroke-width="1.2"/></svg>www.briskfieldacademy.com</li>
  </ul>
</div>
</body>
</html>
```